Product flyer with pricing

We manufacture iconic and luxury vending trailers. for our first trailer we need a flyer created to give to prospective clients with base pricing. I am uploading an example along with graphic files.

```html
<!DOCTYPE html>
<html lang="en">
<head>
<meta charset="utf-8">
<title>The Open Barn House Mini – Nestvend Trailers</title>
<link href="https://fonts.googleapis.com/css2?family=Montserrat:wght@700;800&family=Open+Sans:wght@700;800&family=Ubuntu:wght@400;500;700&display=swap" rel="stylesheet">
<style>
  :root {
    --orange: #e08a22;
    --green: #3b8a3e;
    --green-dark: #2f7a33;
    --sage: #94c08e;
    --peach: #f6d4ac;
    --ink: #1f1f1f;
    --slate: #5d6670;
    --white: #ffffff;
  }
  * { margin: 0; padding: 0; box-sizing: border-box; }
  html, body { width: 848px; height: 1200px; overflow: hidden; background: var(--white); }
  .flyer { position: relative; width: 848px; height: 1200px; overflow: hidden; font-family: "Ubuntu", sans-serif; color: var(--ink); }
  .backdrop { position: absolute; inset: 0; }
  .abs { position: absolute; }

  .brand { left: 62px; top: 96px; display: flex; align-items: center; gap: 8px; }
  .brand-dot { width: 22px; height: 22px; border-radius: 50%; background: var(--orange); }
  .brand-name { font-family: "Montserrat", sans-serif; font-weight: 800; font-size: 23px; color: var(--green-dark); letter-spacing: 0.5px; }

  .title { left: 0; top: 188px; width: 360px; color: var(--white); font-family: "Open Sans", sans-serif; font-weight: 800; }
  .title-kicker { text-align: center; font-size: 34px; width: 320px; line-height: 40px; }
  .title-main { margin-left: 30px; font-size: 55px; line-height: 70px; letter-spacing: -1.5px; white-space: nowrap; margin-top: 8px; }
  .subtitle { left: 32px; top: 398px; color: var(--white); font-family: "Ubuntu", sans-serif; font-weight: 400; font-size: 27px; letter-spacing: 0.3px; white-space: nowrap; }

  .heading { font-family: "Montserrat", sans-serif; font-weight: 800; font-size: 31px; line-height: 36px; letter-spacing: 0.3px; }
  .heading--green { color: var(--green); }
  .heading--orange { color: var(--orange); }
  .features-heading { left: 32px; top: 462px; }
  .price-tag-text { left: 237px; top: 466px; width: 358px; height: 58px; display: flex; align-items: center; justify-content: center; color: var(--white); font-family: "Montserrat", sans-serif; font-weight: 800; font-size: 28px; }

  .bullets { list-style: none; }
  .bullets li { position: relative; font-size: 18px; line-height: 20px; font-weight: 500; padding-left: 22px; white-space: nowrap; }
  .bullets li::before { content: ""; position: absolute; left: 1px; top: 6px; width: 9px; height: 9px; border-radius: 50%; background: var(--orange); }
  .features { left: 32px; top: 535px; }
  .features .wrap { display: block; padding-left: 137px; }

  .usecases-heading { left: 36px; top: 699px; }
  .options-heading { left: 315px; top: 699px; }

  .usecase-box { left: 0; top: 734px; width: 291px; height: 137px; background: var(--peach); padding: 9px 0 0 31px; font-size: 13.6px; line-height: 17.3px; font-weight: 500; }
  .usecase-box .tag { color: var(--orange); font-weight: 400; }
  .usecase-box p { white-space: nowrap; }
  .usecase-box .indent { padding-left: 3px; }
  .usecase-box .small { font-size: 11.6px; letter-spacing: -0.2px; }

  .options { left: 297px; top: 747px; }
  .options li { line-height: 19.6px; }
  .options .price { color: var(--orange); }

  .photo { top: 879px; height: 189px; }

  .rule { left: 0; top: 1068px; width: 848px; height: 11px; background: var(--orange); }
  .footer { left: 0; top: 1079px; width: 848px; height: 98px; background: var(--green); color: var(--white); }
  .footer-item { position: absolute; display: flex; align-items: center; }
  .footer-text { font-size: 21px; line-height: 28px; }
  .contact-address { left: 36px; top: 18px; gap: 18px; }
  .contact-phone { left: 296px; top: 14px; gap: 18px; }
  .phone-text { font-family: "Montserrat", sans-serif; font-weight: 800; text-align: center; font-size: 29px; line-height: 35px; }
  .contact-mail { left: 594px; top: 18px; gap: 16px; }
</style>
</head>
<body>
<div class="flyer">
  <svg class="backdrop" width="848" height="1200" viewBox="0 0 848 1200">
    <defs>
      <linearGradient id="heroTone" x1="0" y1="0" x2="0" y2="1">
        <stop offset="0" stop-color="#6f9ed8"/>
        <stop offset="0.35" stop-color="#b9c6cf"/>
        <stop offset="0.6" stop-color="#e9ecee"/>
        <stop offset="1" stop-color="#7b838a"/>
      </linearGradient>
    </defs>
    <polygon role="img" aria-label="Photo of the white board-and-batten vending house with black door and window, parked on asphalt with trees behind" points="399,0 848,0 848,555 611,555 263,151" fill="url(#heroTone)"/>
    <polygon points="611,555 848,555 848,721" fill="var(--slate)"/>
    <polygon points="0,151 263,151 555,445 0,445" fill="var(--orange)"/>
    <polygon points="237,466 577,466 636,524 237,524" fill="var(--sage)"/>
  </svg>

  <div class="abs brand"><span class="brand-dot"></span><span class="brand-name">NESTVEND TRAILERS</span></div>

  <div class="abs title">
    <div class="title-kicker">THE</div>
    <div class="title-main">OPEN BARN<br>HOUSE MINI</div>
  </div>
  <div class="abs subtitle">LUXURY, MOBILE VENDING HOUSE</div>

  <h2 class="abs heading heading--green features-heading">BASE UNIT<br>FEATURES</h2>
  <div class="abs price-tag-text">BASE PRICE: $45,000</div>

  <ul class="abs bullets features">
    <li>Trailer features tandem wheels w/ brakes.</li>
    <li>Steel frame construction for fire retardation safety and weight reduction.</li>
    <li>100% off grid with solar and lithium battery system allowing the trailer<span class="wrap">to be used in places not accessible by traditional trailers.</span></li>
    <li>80 gallon water supply tank.</li>
    <li>100 gallon waste water tank.</li>
    <li>Cupboards, cabinets &amp; four stainless steel sinks.</li>
    <li>60” Gas shock serving window.</li>
  </ul>

  <h2 class="abs heading heading--orange usecases-heading">USE CASES:</h2>
  <h2 class="abs heading heading--green options-heading">AVAILABLE OPTIONS:</h2>

  <div class="abs usecase-box">
    <p><span class="tag">Food:</span> Lemonade, Coffee, pizza, cookies,</p>
    <p>doughnuts, barbecue and more!</p>
    <p><span class="tag">Retail:</span> Clothing, watchers, jewelry,</p>
    <p class="indent">flowers and more!</p>
    <p><span class="tag">Coporate:</span> Product info, demonstratio,</p>
    <p class="indent">information, brand awareness.</p>
    <p class="small"><span class="tag">Fundraisers:</span> Girls / boy sports, non profits, etc.</p>
  </div>

  <ul class="abs bullets options">
    <li>NVAC - Kelvo Mini Split - <span class="price">$1,800</span></li>
    <li>Cooler / Glass front Commercial refrigerator - <span class="price">$1,600</span></li>
    <li>Upper loft storage area - <span class="price">$1,200</span></li>
    <li>Signage and graphics - <span class="price">$2,000-$5,000</span> depend on complexity</li>
    <li>Ice machine - <span class="price">$1,100</span></li>
    <li>Other custom items available on request.</li>
  </ul>

  <svg class="abs photo" style="left:0" width="284" height="189" role="img" aria-label="Photo of the vending house side view on its tandem-axle trailer hitched to a pickup">
    <defs><linearGradient id="sideA" x1="0" y1="0" x2="0" y2="1"><stop offset="0" stop-color="#7fa6d6"/><stop offset="0.45" stop-color="#e8eaeb"/><stop offset="1" stop-color="#4a4f55"/></linearGradient></defs>
    <rect width="284" height="189" fill="url(#sideA)"/>
  </svg>
  <svg class="abs photo" style="left:296px" width="251" height="189" role="img" aria-label="Photo of a man opening the serving window of the vending house">
    <defs><linearGradient id="sideB" x1="0" y1="0" x2="0" y2="1"><stop offset="0" stop-color="#86aad8"/><stop offset="0.45" stop-color="#e6e8ea"/><stop offset="1" stop-color="#555a60"/></linearGradient></defs>
    <rect width="251" height="189" fill="url(#sideB)"/>
  </svg>
  <svg class="abs photo" style="left:561px" width="287" height="189" role="img" aria-label="Photo of the vending house rear side with shingle roof and windows">
    <defs><linearGradient id="sideC" x1="0" y1="0" x2="0" y2="1"><stop offset="0" stop-color="#8bb0dc"/><stop offset="0.5" stop-color="#eceeef"/><stop offset="1" stop-color="#5b6066"/></linearGradient></defs>
    <rect width="287" height="189" fill="url(#sideC)"/>
  </svg>

  <div class="abs rule"></div>
  <footer class="abs footer">
    <div class="footer-item contact-address">
      <svg width="38" height="46" viewBox="0 0 38 46" aria-hidden="true"><path d="M19 44 C19 44 4 27 4 17 A15 15 0 0 1 34 17 C34 27 19 44 19 44 Z" fill="none" stroke="#fff" stroke-width="3"/><circle cx="19" cy="17" r="6" fill="none" stroke="#fff" stroke-width="3"/></svg>
      <div class="footer-text">123, Main Street,<br>Your City, USA</div>
    </div>
    <div class="footer-item contact-phone">
      <svg width="26" height="50" viewBox="0 0 26 50" aria-hidden="true"><path d="M10 3 L18 3 L18 13 L13 15 C11 20 11 30 13 35 L18 37 L18 47 L10 47 C2 40 2 10 10 3 Z" fill="#fff"/></svg>
      <div class="phone-text">For Bobking<br>+1234567890</div>
    </div>
    <div class="footer-item contact-mail">
      <svg width="46" height="36" viewBox="0 0 46 36" aria-hidden="true"><rect x="2" y="2" width="42" height="32" fill="none" stroke="#fff" stroke-width="3"/><path d="M2 2 L23 21 L44 2 M2 34 L17 16 M44 34 L29 16" fill="none" stroke="#fff" stroke-width="3"/></svg>
      <div class="footer-text">hi@nestvend.com<br>www.nestvend.com</div>
    </div>
  </footer>
</div>
</body>
</html>
```